velmo tarsik

WANTING A DL FLYER DESIGN
Wanting a design to advertise the supply and install of my new VELMO QT TARSIK in dash GPS system.
Wanting pictures on it wilth colours.
This product is going to be sold in NEW CAR dealerships.

My company is all about installing in dash GPS touch screens. made to fit into your dash.

Must state on the flyer:
$995 fitted - Please make the price bold so it stands out
Steering wheel controls still work
DVD/VCD/MP3/SD/USB/melqo/CD/RDS Radio/GPS plus heaps more.
Fits ZB, ZBN ZBW & Moonbrisk
Built into the dash, made to fit!

New car customers

Wheel

• Please incorporate my logo into the flyer. will be uploading later today
My email - tomparvey@mailquist.net
My Phone - 0412 568 214
• wanting the main idea to be based on the stereo picture.

```html
<!DOCTYPE html>
<html lang="en">
<head>
<meta charset="utf-8">
<title>Parvey Fitouts – In-Dash GPS Flyer</title>
<link href="https://fonts.googleapis.com/css2?family=Arimo:ital,wght@0,700;1,700&family=Montserrat:ital,wght@1,900&display=swap" rel="stylesheet">
<style>
  :root {
    --black: #050505;
    --orange: #f08a1c;
    --orange-deep: #e97f10;
    --blue-top: #1f8fd6;
    --blue-mid: #1a5f9e;
    --navy: #1b2440;
    --white: #ffffff;
    --rule: rgba(190, 215, 240, 0.55);
    --logo-blue: #2a8fd8;
  }
  html, body {
    margin: 0;
    padding: 0;
    width: 1200px;
    height: 2470px;
    overflow: hidden;
    background: var(--black);
  }
  .flyer {
    position: relative;
    width: 1200px;
    height: 2470px;
    overflow: hidden;
    background: var(--black);
    font-family: "Arimo", Arial, sans-serif;
  }
  .price {
    position: absolute;
    top: 95px;
    left: 0;
    width: 100%;
    margin: 0;
    text-align: center;
    font-family: "Montserrat", Arial, sans-serif;
    font-style: italic;
    font-weight: 900;
    font-size: 132px;
    line-height: 1;
    color: var(--orange);
    letter-spacing: 2px;
  }
  .stereo-photo {
    position: absolute;
    top: 240px;
    left: 0;
    width: 1200px;
    height: 780px;
    background:
      radial-gradient(ellipse 45% 35% at 50% 30%, #6a7a9a 0%, #3a4256 45%, transparent 75%),
      linear-gradient(180deg, #2a2d33 0%, #4b5059 45%, #2b2e34 100%);
  }
  .wave {
    position: absolute;
    top: 0;
    left: 0;
  }
  .features {
    position: absolute;
    top: 1110px;
    left: 0;
    width: 100%;
    text-align: center;
    color: var(--white);
  }
  .feature {
    margin: 0;
    font-weight: 700;
    font-size: 58px;
    line-height: 72px;
  }
  .rule {
    width: 930px;
    height: 4px;
    margin: 0 auto;
    background: var(--rule);
  }
  .feature--controls { padding-bottom: 62px; }
  .feature--formats { padding: 50px 0 52px; }
  .feature--models { padding: 46px 0 60px; }
  .tagline {
    margin: 0;
    padding-top: 40px;
    font-style: italic;
    font-weight: 700;
    font-size: 58px;
    line-height: 68px;
    color: var(--orange);
  }
  .brand {
    position: absolute;
    top: 2080px;
    left: 0;
    width: 100%;
    display: flex;
    justify-content: center;
    align-items: center;
    gap: 18px;
  }
  .brand__mark {
    width: 70px;
    height: 70px;
    background: var(--logo-blue);
    border-radius: 8px;
  }
  .brand__name {
    font-weight: 700;
    font-size: 52px;
    color: var(--logo-blue);
  }
  .contact-band {
    position: absolute;
    top: 2233px;
    left: 0;
    width: 100%;
    height: 165px;
    background: var(--orange-deep);
    text-align: center;
    color: var(--black);
    font-weight: 700;
    font-size: 54px;
    line-height: 66px;
    padding-top: 17px;
    box-sizing: border-box;
    letter-spacing: 1px;
  }
  .contact-band p { margin: 0; }
</style>
</head>
<body>
<main class="flyer">
  <h1 class="price">$995 fitted</h1>

  <div class="stereo-photo" role="img" aria-label="Photo of the in-dash touch screen stereo fitted in the vehicle dashboard"></div>

  <svg class="wave" width="1200" height="2240" viewBox="0 0 1200 2240" aria-hidden="true">
    <defs>
      <linearGradient id="blueFade" x1="0" y1="0" x2="0" y2="1">
        <stop offset="0" stop-color="#1f8fd6"/>
        <stop offset="0.35" stop-color="#1a73b8"/>
        <stop offset="0.7" stop-color="#1c3d6e"/>
        <stop offset="1" stop-color="#1b2440"/>
      </linearGradient>
    </defs>
    <path d="M0 720 C 300 900, 750 1010, 1200 930 L1200 2240 L0 2240 Z" fill="url(#blueFade)"/>
    <path d="M0 720 C 300 900, 750 1010, 1200 930" fill="none" stroke="#f08a1c" stroke-width="26"/>
  </svg>

  <section class="features">
    <p class="feature feature--controls">Steering wheel<br>controls still work</p>
    <div class="rule"></div>
    <p class="feature feature--formats">DVD/VCD/MP3/SD/USB/mel<br>qo/CD/RDS Radio/GPS<br>plus heaps more.</p>
    <div class="rule"></div>
    <p class="feature feature--models">Fits ZB, ZBN ZBW &amp;<br>Moonbrisk</p>
    <div class="rule"></div>
    <p class="tagline">Built into the dash,<br>made to fit!</p>
  </section>

  <div class="brand">
    <span class="brand__mark"></span>
    <span class="brand__name">Parvey Fitouts</span>
  </div>

  <footer class="contact-band">
    <p>tomparvey@mailquist.net</p>
    <p>0412 568 214</p>
  </footer>
</main>
</body>
</html>
```